Postcard Design - Thank you for your referral

We are a construction and remodeling company that does everything from frame to finish. We have a logo that we would like to incorporate. We want to be able to quickly thank our friends and clients for the kind referrals.
Target Market(s)
clients, friends and family that trust us enough to refer us
Industry/Entity Type
Construction
Requirements
Must have
- Must match our current colors/logo, etc.
No "cartoon-like" stuff
No "catch phrase" stuff
nothing "cutesy" for example we received one from a company recently with army tanks on the front that said "tanks for your business" - definitely not our style
Should not have
- cartoon characters
cutesy play on words
nothing old fashioned

```html
<!DOCTYPE html>
<html lang="en">
<head>
<meta charset="utf-8">
<title>Northgate Construction &amp; Remodeling – Referral Postcard</title>
<link rel="stylesheet" href="https://fonts.googleapis.com/css2?family=Open+Sans:wght@400;600&family=Alegreya:ital,wght@1,500&display=swap">
<style>
  :root {
    --navy: #15254a;
    --navy-deep: #0f1c3a;
    --orange: #e0692a;
    --white: #ffffff;
    --paper: #ffffff;
    --backdrop: #ebe6de;
    --rule: #b9b9b9;
    --ink-soft: #6b6b6b;
  }
  * { margin: 0; padding: 0; box-sizing: border-box; }
  html, body {
    width: 947px;
    height: 1200px;
    overflow: hidden;
    background: var(--backdrop);
    font-family: "Open Sans", Arial, sans-serif;
  }
  .canvas { position: relative; width: 947px; height: 1200px; }

  /* Front of the postcard */
  .postcard-front {
    position: absolute;
    left: 164px; top: 44px;
    width: 663px; height: 510px;
    background: var(--navy);
    color: var(--white);
    box-shadow: 0 3px 8px rgba(0,0,0,.25);
  }
  .tagline {
    position: absolute;
    top: 60px; left: 0; width: 100%;
    text-align: center;
    font-size: 21px;
    letter-spacing: .2px;
  }
  .brand-front {
    position: absolute;
    left: 62px; top: 138px;
    display: flex; align-items: center; gap: 30px;
  }
  .brand-mark-front { width: 64px; height: 64px; background: var(--white); }
  .brand-name-front {
    font-weight: 600;
    color: var(--white);
    font-size: 38px;
    line-height: 1.05;
  }
  .brand-name-front span { display: block; font-size: 26px; }
  .site-front {
    position: absolute;
    left: 222px; top: 297px;
    font-size: 14px;
    color: var(--orange);
  }
  .referral-band {
    position: absolute;
    left: 0; top: 366px;
    width: 100%; height: 72px;
    border-top: 3px solid var(--orange);
  }
  .referral-band .band {
    position: absolute;
    left: 0; top: 8px; width: 100%; height: 56px;
    background: var(--orange);
    border-top: 2px solid var(--navy-deep);
    border-bottom: 2px solid var(--navy-deep);
    display: flex; align-items: center; justify-content: center;
  }
  .referral-band h1 {
    font-family: "Alegreya", Georgia, serif;
    font-style: italic;
    font-weight: 500;
    font-size: 40px;
    letter-spacing: 1px;
  }
  .contact {
    position: absolute;
    left: 26px; top: 447px;
    font-size: 15px;
    line-height: 21px;
  }
  .owner {
    position: absolute;
    right: 36px; top: 458px;
    font-size: 22px;
  }
  .owner small { font-size: 13px; margin-left: 14px; }

  /* Back of the postcard */
  .postcard-back {
    position: absolute;
    left: 166px; top: 602px;
    width: 659px; height: 509px;
    background: var(--paper);
    box-shadow: 0 3px 8px rgba(0,0,0,.2);
  }
  .brand-back {
    position: absolute;
    left: 30px; top: 26px;
    display: flex; align-items: center; gap: 14px;
  }
  .brand-mark-back { width: 36px; height: 36px; background: var(--navy); }
  .brand-name-back {
    font-weight: 600;
    color: var(--navy);
    font-size: 22px;
    line-height: 1.05;
  }
  .brand-name-back span { display: block; font-size: 15px; }
  .site-back {
    position: absolute;
    left: 118px; top: 94px;
    font-size: 11px;
    font-weight: 600;
    color: var(--orange);
  }
  .stamp-box {
    position: absolute;
    left: 511px; top: 19px;
    width: 119px; height: 92px;
    border: 1.5px solid var(--rule);
  }
  .address-lines {
    position: absolute;
    left: 409px; top: 217px;
    width: 219px;
  }
  .address-lines li {
    list-style: none;
    height: 42px;
    border-top: 1.5px solid var(--rule);
  }
</style>
</head>
<body>
<main class="canvas">
  <section class="postcard-front" aria-label="Postcard front">
    <p class="tagline">Innovative Designs and Complete Remodeling Solutions</p>
    <div class="brand-front">
      <div class="brand-mark-front"></div>
      <div class="brand-name-front">Northgate<span>Construction &amp; Remodeling, LLC</span></div>
    </div>
    <p class="site-front">www.northgatebuilds.com</p>
    <div class="referral-band">
      <div class="band"><h1>Thank You For Your Referral</h1></div>
    </div>
    <p class="contact">555-014-2290<br>dan@northgatebuilds.com</p>
    <p class="owner">Daniel Marsh<small>owner</small></p>
  </section>

  <section class="postcard-back" aria-label="Postcard back">
    <div class="brand-back">
      <div class="brand-mark-back"></div>
      <div class="brand-name-back">Northgate<span>Construction &amp; Remodeling, LLC</span></div>
    </div>
    <p class="site-back">www.northgatebuilds.com</p>
    <div class="stamp-box"></div>
    <ul class="address-lines">
      <li></li><li></li><li></li><li></li>
    </ul>
  </section>
</main>
</body>
</html>
```